Billboard for Real Estate Agent

I need a signage design for my billboard that is going up end of December.

-I target the higher end waterfront properties ($1,000,000 +) in Corella Bend, QLD, Australia so it needs to be sleek, funky yet sophisticated and professional and needs to have my photo- or if you have an idea with someone else's photo, then I can have one taken that's the same.

-The purpose is to target those who are thinking about selling/buying property.
We want people to remember the ad, so it's top of mind.

-The billboard is on the side of the road, and will be lit up at night and I'll have it for 13 months. Needs to be noticeable from the road, but nothing tacky and too loud.

Needs to have my name, Mara Pendleby and my contact number and business logo (attached).

Mara Pendleby
0462 913 517

Target Market(s)

Wealthy demographic 25-65 years old.

Industry/Entity Type

Business

Requirements
Must have
• My name, phone number and HOMVEX logo attached.

Bix Guidelines:
http://www.bixmedia.example/our-resources/artwork-guidelines/

Heading: Don't be a Dinosaur
Subline: Think Differently

Use one of the photos.
Nice to have
• -Quirky, different and captivating (i've attached some wacky billboard ideas)

```html
<!DOCTYPE html>
<html lang="en">
<head>
<meta charset="utf-8">
<title>Mara Pendleby – Billboard Options</title>
<link rel="stylesheet" href="https://fonts.googleapis.com/css2?family=Alfa+Slab+One&family=Archivo+Black&family=Arimo:wght@700&family=Tangerine:wght@700&display=swap">
<style>
  :root {
    --stage: #d7d9db;
    --blue-deep: #0b5f9c;
    --blue-mid: #1690cf;
    --blue-bright: #2fb6ea;
    --band-light: #5fd0f2;
    --band-dark: #0a4f86;
    --ink: #151515;
    --white: #ffffff;
    --yellow: #fff200;
    --label-red: #e3161b;
    --photo-a: #7fd3ef;
    --photo-b: #1d7f86;
  }
  * { margin: 0; padding: 0; box-sizing: border-box; }
  html, body { width: 1200px; height: 514px; overflow: hidden; background: var(--stage); }
  .canvas { position: relative; width: 1200px; height: 514px; }

  .board {
    position: absolute; overflow: hidden;
    border: 3px solid var(--white);
    background: radial-gradient(ellipse at 70% 40%, var(--blue-bright) 0%, var(--blue-mid) 45%, var(--blue-deep) 100%);
    box-shadow: 0 2px 6px rgba(0,0,0,.35);
  }
  .board--one { left: 35px; top: 22px; width: 593px; height: 253px; }
  .board--two { left: 697px; top: 7px; width: 496px; height: 243px; }
  .board--three { left: 697px; top: 262px; width: 496px; height: 240px; }

  .portrait {
    position: absolute; top: 0; bottom: 0; right: 0;
    background: linear-gradient(160deg, var(--photo-a) 0%, #3aa7c9 50%, var(--photo-b) 100%);
  }
  .board--one .portrait { width: 203px; }
  .board--two .portrait { width: 146px; }
  .board--three .portrait { width: 176px; }

  .headline-top, .headline-main {
    position: absolute; font-family: "Alfa Slab One", serif; color: var(--ink);
    text-shadow: 2px 0 0 var(--white), -2px 0 0 var(--white), 0 2px 0 var(--white), 0 -2px 0 var(--white);
    line-height: 1; white-space: nowrap; text-transform: uppercase;
  }
  .subline {
    position: absolute; font-family: "Tangerine", cursive; font-weight: 700;
    color: var(--ink); line-height: 1; white-space: nowrap;
  }
  .name-first {
    position: absolute; font-family: "Archivo Black", sans-serif; color: var(--yellow);
    letter-spacing: 2px; line-height: 1; text-shadow: 1px 1px 2px rgba(0,0,0,.4);
  }
  .name-last {
    position: absolute; font-family: "Arimo", sans-serif; font-weight: 700;
    color: var(--white); line-height: 1; text-shadow: 1px 1px 2px rgba(0,0,0,.4);
  }
  .phone {
    position: absolute; display: flex; align-items: center; gap: 8px;
    font-family: "Arimo", sans-serif; font-weight: 700; color: var(--yellow); line-height: 1;
  }
  .phone svg { fill: var(--yellow); }
  .brand {
    position: absolute; display: flex; align-items: center; gap: 6px;
    font-family: "Arimo", sans-serif; font-weight: 700; color: var(--white); line-height: 1;
  }
  .brand-dot { border-radius: 50%; background: var(--white); }

  .contact-band { position: absolute; left: 0; background: linear-gradient(90deg, rgba(95,208,242,.55), rgba(95,208,242,.2)); }
  .address-band {
    position: absolute; left: 0; right: 0; bottom: 0; height: 30px;
    background: var(--band-dark); color: var(--white);
    font-family: "Arimo", sans-serif; font-weight: 700; font-size: 13px;
    display: flex; align-items: center; padding-left: 30px;
  }

  .option-label {
    position: absolute; font-family: "Arimo", sans-serif; font-weight: 700; color: var(--label-red);
    text-shadow: 2px 0 0 var(--white), -2px 0 0 var(--white), 0 2px 0 var(--white), 0 -2px 0 var(--white);
    line-height: 1; white-space: nowrap;
  }
</style>
</head>
<body>
<main class="canvas">

  <!-- Option 1 -->
  <section class="board board--one">
    <div class="portrait" role="img" aria-label="Portrait photo of the agent smiling, wearing a teal top"></div>
    <div class="contact-band" style="top:203px;width:395px;height:47px;"></div>
    <div class="headline-top" style="left:20px;top:14px;font-size:27px;">Don't be a</div>
    <div class="headline-main" style="left:18px;top:40px;font-size:60px;letter-spacing:1px;">Dinosaur</div>
    <div class="subline" style="left:188px;top:92px;font-size:38px;">...Do things differently</div>
    <div class="name-first" style="left:52px;top:128px;font-size:38px;">MARA</div>
    <div class="name-last" style="left:26px;top:166px;font-size:29px;">PENDLEBY</div>
    <div class="phone" style="left:16px;top:216px;font-size:26px;">
      <svg width="28" height="22" viewBox="0 0 28 22" aria-hidden="true"><path d="M2 7c0-4 5-6 12-6s12 2 12 6v2h-7V6H9v3H2z"/><path d="M7 10h14l4 11H3z"/></svg>
      <span>0462.913.517</span>
    </div>
    <div class="brand" style="left:268px;top:214px;font-size:21px;"><span class="brand-dot" style="width:16px;height:16px;"></span>HOMVEX</div>
  </section>
  <div class="option-label" style="left:430px;top:378px;font-size:33px;">OPTION 1</div>

  <!-- Option 2 -->
  <section class="board board--two">
    <div class="portrait" role="img" aria-label="Portrait photo of the agent smiling, wearing a teal top"></div>
    <div class="headline-top" style="left:38px;top:30px;font-size:22px;">Don't be a</div>
    <div class="headline-main" style="left:36px;top:52px;font-size:47px;">Dinosaur</div>
    <div class="subline" style="left:166px;top:88px;font-size:30px;">...Do things differently</div>
    <div class="name-first" style="left:74px;top:118px;font-size:28px;">MARA</div>
    <div class="name-last" style="left:58px;top:146px;font-size:19px;">PENDLEBY</div>
    <div class="brand" style="left:222px;top:130px;font-size:19px;"><span class="brand-dot" style="width:14px;height:14px;"></span>HOMVEX</div>
    <div class="phone" style="left:38px;top:172px;font-size:26px;">
      <svg width="28" height="22" viewBox="0 0 28 22" aria-hidden="true"><path d="M2 7c0-4 5-6 12-6s12 2 12 6v2h-7V6H9v3H2z"/><path d="M7 10h14l4 11H3z"/></svg>
      <span>0462.913.517</span>
    </div>
    <div class="address-band">Located 4216 Corella Bend, Tidewater St.</div>
  </section>
  <div class="option-label" style="left:931px;top:6px;font-size:22px;">OPTION 2</div>

  <!-- Option 3 -->
  <section class="board board--three">
    <div class="portrait" role="img" aria-label="Portrait photo of the agent smiling, wearing a teal top"></div>
    <div class="headline-top" style="left:38px;top:24px;font-size:22px;">Don't be a</div>
    <div class="headline-main" style="left:36px;top:46px;font-size:47px;">Dinosaur</div>
    <div class="subline" style="left:170px;top:82px;font-size:30px;">...Do things differently</div>
    <div class="brand" style="left:32px;top:124px;font-size:19px;"><span class="brand-dot" style="width:14px;height:14px;"></span>HOMVEX</div>
    <div class="name-first" style="left:214px;top:118px;font-size:26px;">MARA</div>
    <div class="name-last" style="left:200px;top:145px;font-size:19px;">PENDLEBY</div>
    <div class="phone" style="left:38px;top:168px;font-size:26px;">
      <svg width="28" height="22" viewBox="0 0 28 22" aria-hidden="true"><path d="M2 7c0-4 5-6 12-6s12 2 12 6v2h-7V6H9v3H2z"/><path d="M7 10h14l4 11H3z"/></svg>
      <span>0462.913.517</span>
    </div>
    <div class="address-band">Located 4216 Corella Bend, Tidewater St.</div>
  </section>
  <div class="option-label" style="left:931px;top:270px;font-size:22px;">OPTION 3</div>

</main>
</body>
</html>
```